Webdesign für Personalvermittlung
Zielgruppe
Personalvermittlung
Aufgabenstellung
es soll einladend - nicht zu überladen und natürlich cool und modern sein

```html
<!DOCTYPE html>
<html lang="de">
<head>
<meta charset="utf-8">
<title>Pflegepfad – Karriere im Pflegeberuf</title>
<link rel="stylesheet" href="https://fonts.googleapis.com/css2?family=Rubik:wght@400;500;600&display=swap">
<style>
  :root {
    --green: #5cb845;
    --blue: #1f97dc;
    --ink: #2f3337;
    --muted: #55595e;
    --line: #e6e8ea;
    --paper: #ffffff;
    --footer: #f3f4f5;
  }
  * { box-sizing: border-box; margin: 0; padding: 0; }
  html, body { width: 1200px; height: 3500px; overflow: hidden; }
  body { font-family: "Rubik", Arial, sans-serif; color: var(--ink); background: var(--paper); }
  .page { position: relative; width: 1200px; height: 3500px; }
  section, footer { position: absolute; left: 0; width: 1200px; }
  .shape { position: absolute; left: 0; top: 0; }

  /* brand */
  .brand { display: flex; align-items: center; gap: 10px; font-weight: 600; font-size: 15px; letter-spacing: .5px; color: var(--ink); }
  .brand-mark { width: 22px; height: 22px; background: var(--green); border-radius: 4px; }

  /* hero */
  .hero { top: 0; height: 820px; }
  .hero .brand { position: absolute; left: 125px; top: 42px; }
  .nav { position: absolute; right: 110px; top: 48px; display: flex; gap: 38px; }
  .nav a { color: #fff; font-size: 14px; font-weight: 500; text-decoration: none; }
  .hero-copy { position: absolute; left: 125px; top: 255px; width: 420px; }
  .hero-title { font-size: 38px; font-weight: 500; line-height: 1.2; text-transform: uppercase; }
  .hero-title .accent { color: var(--green); }
  .hero-lead { margin-top: 26px; font-size: 17px; line-height: 1.5; color: var(--muted); width: 300px; }
  .hero-actions { margin-top: 34px; display: flex; align-items: center; gap: 30px; }
  .btn { display: inline-flex; align-items: center; gap: 8px; background: var(--blue); color: #fff; border-radius: 20px; font-size: 14px; padding: 9px 22px; }
  .link { color: var(--green); font-size: 14px; display: inline-flex; align-items: center; gap: 6px; }
  .hero-video { position: absolute; left: 560px; top: 235px; width: 560px; height: 395px; border-radius: 4px;
    background: linear-gradient(135deg, #d9c6bf 0%, #eae7e6 35%, #8c97a3 70%, #c7cbd0 100%);
    display: flex; align-items: center; justify-content: center; overflow: hidden; }
  .hero-video span { font-size: 110px; font-weight: 400; color: rgba(80,84,90,.55); transform: rotate(-35deg); letter-spacing: 4px; }

  /* section head */
  .eyebrow { color: var(--green); font-size: 16px; text-transform: uppercase; letter-spacing: .3px; }
  .section-title { font-size: 31px; font-weight: 500; text-transform: uppercase; margin-top: 4px; line-height: 1.15; }

  /* services */
  .services { top: 820px; height: 880px; }
  .services .head { position: absolute; left: 125px; top: 20px; }
  .cards { position: absolute; left: 125px; top: 140px; width: 975px; display: grid; grid-template-columns: repeat(3, 300px); column-gap: 37px; row-gap: 28px; }
  .card { background: #fff; border-radius: 6px; box-shadow: 0 3px 14px rgba(0,0,0,.10); padding: 20px 18px 22px; height: 300px; }
  .card-head { display: flex; align-items: flex-start; gap: 14px; margin-bottom: 18px; min-height: 48px; }
  .card-head svg { flex: none; width: 38px; height: 30px; }
  .card-title { font-size: 18px; font-weight: 500; line-height: 1.25; }
  .card p { font-size: 13.5px; line-height: 1.95; color: var(--muted); }

  /* testimonials */
  .testimonials { top: 1700px; height: 520px; }
  .testimonials .head { position: absolute; left: 125px; top: 30px; }
  .testimonials .intro { position: absolute; left: 125px; top: 190px; width: 300px; font-size: 14px; line-height: 1.95; color: var(--muted); }
  .testimonials .intro .btn { margin-top: 20px; }
  .quote-card { position: absolute; left: 460px; top: 175px; width: 640px; background: #fff; border-radius: 6px; box-shadow: 0 3px 14px rgba(0,0,0,.10); padding: 22px 22px 26px; }
  .quote-head { display: flex; gap: 14px; align-items: center; }
  .quote-name { font-size: 18px; font-weight: 500; }
  .quote-role { font-size: 12px; color: var(--muted); }
  .quote-card p { margin-top: 18px; font-size: 13.5px; line-height: 1.95; color: var(--muted); }

  /* contact */
  .contact { top: 2220px; height: 1100px; }
  .contact-photo { position: absolute; left: 125px; top: 110px; width: 480px; height: 480px;
    background: linear-gradient(160deg, #e9edf1 0%, #cfd6dc 45%, #8a9098 75%, #b9c3cf 100%); }
  .contact .head { position: absolute; left: 640px; top: 100px; }
  .form { position: absolute; left: 640px; top: 270px; width: 480px; display: grid; grid-template-columns: 1fr 1fr; gap: 14px 20px; }
  .field { background: #fff; border-radius: 18px; height: 32px; font-size: 13px; color: #9aa0a6; display: flex; align-items: center; justify-content: space-between; padding: 0 14px; }
  .field.dark { color: var(--ink); }
  .field.full { grid-column: 1 / 3; }
  .field.area { height: 170px; align-items: flex-start; padding-top: 10px; border-radius: 16px; }
  .form .btn { grid-column: 1 / 3; justify-self: start; margin-top: 20px; }

  /* footer */
  .site-footer { top: 3320px; height: 180px; background: var(--footer); }
  .site-footer .brand { position: absolute; left: 160px; top: 70px; }
  .site-footer .nav { top: 74px; right: 120px; }
  .site-footer .nav a { color: var(--ink); }
</style>
</head>
<body>
<div class="page">

  <section class="hero">
    <svg class="shape" width="1200" height="820" aria-hidden="true">
      <polygon points="730,0 1200,0 1200,540 880,540" fill="var(--green)"/>
    </svg>
    <div class="brand"><span class="brand-mark"></span>PFLEGEPFAD</div>
    <nav class="nav"><a href="#">Home</a><a href="#">Bewerber über uns</a><a href="#">Wir über uns</a></nav>
    <div class="hero-copy">
      <h1 class="hero-title">Dein nächster<br><span class="accent">Karriereschritt</span><br>im Pflegeberuf!</h1>
      <p class="hero-lead">Wir bieten Dir den perfekten Job als Führungskraft!</p>
      <div class="hero-actions">
        <span class="btn">Angebot bekommen</span>
        <span class="link">Wir bieten dir
          <svg width="16" height="10" viewBox="0 0 16 10"><path d="M0 5h14M10 1l4 4-4 4" stroke="currentColor" stroke-width="1.4" fill="none"/></svg></span>
      </div>
    </div>
    <div class="hero-video" role="img" aria-label="Videofläche: Arzt im weißen Kittel mit Stethoskop"><span>VIDEO</span></div>
  </section>

  <section class="services">
    <svg class="shape" width="1200" height="880" aria-hidden="true">
      <polygon points="0,260 330,260 830,780 0,780" fill="var(--green)"/>
    </svg>
    <div class="head">
      <div class="eyebrow">Unser Service</div>
      <h2 class="section-title">Was darfst du von uns erwarten?</h2>
    </div>
    <div class="cards">
      <article class="card">
        <div class="card-head">
          <svg viewBox="0 0 38 30" fill="none" stroke="var(--green)" stroke-width="1.8"><circle cx="13" cy="9" r="5"/><path d="M3 27c0-6 4-9 10-9s10 3 10 9"/><circle cx="27" cy="8" r="4"/><path d="M26 16c6 0 9 3 9 8"/></svg>
          <div class="card-title">Zugriff auf mehr<br>Stellen</div>
        </div>
        <p>In Zusammenarbeit mit Einrichtungen und Kliniken erhalten unsere Kandidaten einen zugesicherten Bonus in Höhe von 750 EUR für das Vertrauen bei Ihrem Jobwechsel in pflegepfad.de</p>
      </article>
      <article class="card">
        <div class="card-head">
          <svg viewBox="0 0 38 30" fill="none" stroke="var(--green)" stroke-width="1.8"><rect x="2" y="6" width="34" height="18" rx="2"/><circle cx="19" cy="15" r="5"/><path d="M6 10h3M29 20h3"/></svg>
          <div class="card-title">100 % kostenfrei</div>
        </div>
        <p>Unsere Dienstleistung ist für Dich als Bewerber 100% kostenfrei! Es gibt auch garantiert keine versteckten Kosten!</p>
      </article>
      <article class="card">
        <div class="card-head">
          <svg viewBox="0 0 38 30" fill="none" stroke="var(--green)" stroke-width="1.8"><path d="M2 8h7l4 12H2zM36 8h-7l-4 12h11z"/><path d="M9 9l7-3 6 2 6 1M13 19l5 4 3-2 3 1 3-3"/></svg>
          <div class="card-title">Alle Versprechen<br>im Arbeitsvertrag</div>
        </div>
        <p>Du stellst Bedingungen an deinen neuen Arbeitgeber? - dann sorgen wir gemeinsam dafür, dass Du diese auch im Arbeitsvertrag findest - zu Deiner Sicherheit. Nichts ist schlimmer, als leere Versprechungen!</p>
      </article>
      <article class="card">
        <div class="card-head">
          <svg viewBox="0 0 38 30" fill="none" stroke="var(--green)" stroke-width="1.8"><path d="M3 4h20v13H11l-5 5v-5H3z"/><path d="M26 10h9v13h-3v4l-4-4H17v-3"/></svg>
          <div class="card-title">Dauerhafte<br>Betreuung</div>
        </div>
        <p>Dein neuer Arbeitgeber hält nicht was er verspricht? Keine Sorge, wir werden für Dich sofort wieder aktiv und bieten Dir schnell neue Möglichkeiten an - ohne dass Du erneut Bewerbungen versenden musst! Ein Anruf oder eine Email genügt!</p>
      </article>
      <article class="card">
        <div class="card-head">
          <svg viewBox="0 0 38 30" fill="none" stroke="var(--green)" stroke-width="1.8"><circle cx="19" cy="15" r="12"/><path d="M19 8v9M19 20v2"/></svg>
          <div class="card-title">Anonymität</div>
        </div>
        <p>Wir erstellen ein Profil Deiner Kenntnisse und Fähigkeiten sowie Deiner Berufserfahrung. Weder Dein Name, noch Deine Vorarbeitgeber tauchen im ersten Schritt auf. Erst wenn eine Einrichtung oder Klinik daran Interesse zeigt, entscheiden wir gemeinsam, wie es weitergeht!</p>
      </article>
      <article class="card">
        <div class="card-head">
          <svg viewBox="0 0 38 30" fill="none" stroke="var(--green)" stroke-width="1.8"><path d="M8 9a12 12 0 1 1-1 10"/><path d="M6 4v6h6"/><path d="M19 9v7l5 3"/></svg>
          <div class="card-title">Keine Zeitarbeit</div>
        </div>
        <p>Wir vermitteln ausschließlich in Festanstellungen direkt bei Kliniken oder Einrichtungen. Wir können Dir jedoch wertvolle Tipps geben, sollte Zeitarbeit für Dich in Frage kommen … WIR KENNEN UNS AUS!</p>
      </article>
    </div>
  </section>

  <section class="testimonials">
    <div class="head">
      <div class="eyebrow">Testimonials</div>
      <h2 class="section-title">Was Bewerber über uns sagen</h2>
    </div>
    <div class="intro">
      Durch die Stimmen unserer zufriedenen Kunden erhalten Sie einen ehrlichen Eindruck davon, wie wir arbeiten und welchen Wert wir unseren Kunden bieten.
      <br><span class="btn">Mehr Erfahrungen
        <svg width="16" height="10" viewBox="0 0 16 10"><path d="M0 5h14M10 1l4 4-4 4" stroke="#fff" stroke-width="1.4" fill="none"/></svg></span>
    </div>
    <article class="quote-card">
      <div class="quote-head">
        <svg width="34" height="26" viewBox="0 0 34 26" aria-hidden="true"><path d="M2 26V14C2 6 6 2 14 1v5c-4 1-6 3-6 7h6v13zM20 26V14c0-8 4-12 12-13v5c-4 1-6 3-6 7h6v13z" fill="var(--green)"/></svg>
        <div><div class="quote-name">Max Muster</div><div class="quote-role">Leitung Musterbereich</div></div>
      </div>
      <p>Lorem ipsum dolor sit amet, consetetur sadipscing elitr, sed diam nonumy eirmod tempor invidunt ut labore et dolore magna aliquyam erat, sed diam voluptua. At vero eos et accusam et justo duo dolores et ea rebum. Stet clita kasd gubergren, no sea takimata sanctus est Lorem ipsum dolor sit amet.</p>
    </article>
  </section>

  <section class="contact">
    <svg class="shape" width="1200" height="1100" aria-hidden="true">
      <polygon points="605,240 1200,240 1200,860 470,860 605,640" fill="var(--green)"/>
    </svg>
    <div class="contact-photo" role="img" aria-label="Foto: fröhliche Gruppe junger Menschen in einem hellen Raum"></div>
    <div class="head">
      <div class="eyebrow">Kontakt</div>
      <h2 class="section-title">Wir freuen uns auf<br>dich</h2>
    </div>
    <form class="form">
      <div class="field">Vorname*</div>
      <div class="field">Nachname*</div>
      <div class="field full">E-Mail*</div>
      <div class="field dark">Rückruf erwünscht?
        <svg width="14" height="9" viewBox="0 0 14 9"><path d="M1 1l6 6 6-6" stroke="#2f3337" stroke-width="1.8" fill="none"/></svg></div>
      <div class="field dark">Lebenslauf hochladen
        <svg width="16" height="14" viewBox="0 0 16 14" fill="none" stroke="#2f3337" stroke-width="1.4"><path d="M5 2h10M5 7h10M5 12h10"/><circle cx="1.5" cy="2" r="1"/><circle cx="1.5" cy="7" r="1"/><circle cx="1.5" cy="12" r="1"/></svg></div>
      <div class="field full area">Nachricht</div>
      <span class="btn">Absenden
        <svg width="18" height="13" viewBox="0 0 18 13" fill="none" stroke="#fff" stroke-width="1.4"><rect x="1" y="1" width="16" height="11" rx="1.5"/><path d="M1 2l8 6 8-6"/></svg></span>
    </form>
  </section>

  <footer class="site-footer">
    <div class="brand"><span class="brand-mark"></span>PFLEGEPFAD</div>
    <nav class="nav"><a href="#">Home</a><a href="#">Bewerber über uns</a><a href="#">Wir über uns</a></nav>
  </footer>

</div>
</body>
</html>
```